Business card design needed

The company name is Pellwick Architects. We are an architectural company based in Melbourne,Australia that has a mix of client base from health care, commercial office, aged care, multi-residential, single residential and retail. Design type is contemporary.

Suggest the base colours need to be black and white. Please leave an area on the back of the card available for handwritten notes.

Target Market(s)

Generally corporate, aged 30 to 65

Industry/Entity Type

Residential

Contact Information for Business Card

Pellwick Architects
Dane Pellwick
7 Horbury Street
Northvale VIC 3059
T (03) 9572 4016
M 0431 607 295
E dp@pellwickarc.com.au

Logo Text

PA

Logo styles of interest
Emblem Logo
Abstract Logo
Lettermark Logo
Requirements
Must have
• I am having trouble attaching a sketch so would really appreciate your effort to try the following brief.

Black and White (B&W)
Would like different card cutout profile. Logo Example, use the half circle curve of the G to form the left edge of the card with no margin. The A is to sit inside the G, connected to the G by its horizontal. The A has its cross bar and lower right leg removed. Card in black, text in white.

Back of card to be black text on white background with services provided.

Client Focused Service
Architecture and Design
Functional Planning
Town Planning
Feasability Studies
Contract Documentation
Contract Administration
Project Management

Simple elegant text, Ariel or similar
Nice to have
• Integrated logo and card cut-out.

Card base black on front, white on back
Should not have
• Too many colours
Fussy details

```html
<!DOCTYPE html>
<html lang="en">
<head>
<meta charset="utf-8">
<title>Pellwick Architects – Business Card</title>
<link href="https://fonts.googleapis.com/css2?family=Arimo:wght@400;700&display=swap" rel="stylesheet">
<style>
  :root {
    --backdrop: #939598;
    --card-dark: #3b3a3c;
    --paper: #ffffff;
    --ink: #3b3a3c;
    --faint-mark: #e3e3e4;
  }
  * { margin: 0; padding: 0; box-sizing: border-box; }
  html, body {
    width: 1200px; height: 590px; overflow: hidden;
    background: var(--backdrop);
    font-family: "Arimo", Arial, sans-serif;
  }
  .stage { position: relative; width: 1200px; height: 590px; }

  /* Front of card */
  .front-card {
    position: absolute; left: 230px; top: 162px;
    width: 385px; height: 300px;
    background: var(--card-dark);
  }
  .front-emblem {
    position: absolute; left: 80px; top: 162px;
    width: 300px; height: 300px; border-radius: 50%;
    background: var(--paper);
    display: flex; align-items: center; justify-content: center;
    font-size: 150px; font-weight: 700; color: var(--ink);
    letter-spacing: -4px;
  }
  .label {
    position: absolute; background: var(--paper); color: var(--ink);
    font-size: 14.5px; line-height: 19px;
  }
  .company-label {
    left: 380px; top: 214px; width: 235px; height: 27px;
    font-weight: 700; font-size: 17.5px; line-height: 27px;
    padding-left: 13px; letter-spacing: 0.2px;
  }
  .address-label {
    left: 380px; top: 336px; width: 235px; height: 40px;
    padding: 1px 0 0 12px; font-size: 14px;
  }
  .contact-label {
    left: 439px; top: 389px; width: 176px; height: 58px;
    padding: 2px 9px 0 0; text-align: right; font-size: 14px; line-height: 18px;
  }

  /* Back of card */
  .back-card { position: absolute; left: 782px; top: 58px; }
  .back-mark {
    position: absolute; left: 782px; top: 238px; width: 300px;
    text-align: center; font-size: 90px; font-weight: 400;
    color: var(--faint-mark);
  }
  .back-title {
    position: absolute; left: 782px; top: 470px; width: 300px;
    text-align: center; font-weight: 700; font-size: 17.5px; color: var(--ink);
  }
  .back-title span {
    display: inline-block; border-bottom: 2px solid var(--ink);
    padding: 0 2px 1px;
  }
  .services {
    position: absolute; left: 782px; top: 497px; width: 300px;
    list-style: none; text-align: center;
    font-size: 10.3px; line-height: 15px; color: #222;
  }
  .services .sep { color: #999; padding: 0 1px; }
</style>
</head>
<body>
<main class="stage">
  <div class="front-card"></div>
  <div class="front-emblem">PA</div>
  <div class="label company-label">PELLWICK ARCHITECTS</div>
  <div class="label address-label">Pellwick Architects Dane Pellwick 7<br>Horbury Street Northvale VIC 3059</div>
  <div class="label contact-label">T (03) 9572 4016<br>M 0431 607 295<br>E dp@pellwickarc.com.au</div>

  <svg class="back-card" width="300" height="506" viewBox="0 0 300 506">
    <path d="M0 506 L0 140 Q0 0 150 0 Q300 0 300 140 L300 506 Z" fill="var(--paper)"/>
  </svg>
  <div class="back-mark">PA</div>
  <div class="back-title"><span>PELLWICK ARCHITECTS</span></div>
  <ul class="services">
    <li>Client Focused Service</li>
    <li>Architecture and Design<span class="sep">|</span>Contract Administration</li>
    <li>Project Management<span class="sep">|</span>Town Planning<span class="sep">|</span>Feasability Studies</li>
    <li>Contract Documentation<span class="sep">|</span>Functional Planning</li>
  </ul>
</main>
</body>
</html>
```